Brightnest Dwelling Stationery Design

Letterpaper, business cards, notebook, envelope A4 & A5

Target Market(s)

Business, accommodation, hotels, flexible housing

Font styles to use
Other font styles liked:
• Montserrat

Colors

Designer to choose only greyscale colors for use in the design.

Requirements
Must have
• Luxurious appearance
Keep it simple, just like the logo
Modern
Nice to have
• Tight Luxury Design
Should not have
• Illustrations
Decorative

```html
<!DOCTYPE html>
<html lang="en">
<head>
<meta charset="utf-8">
<title>Brightnest Dwelling — Business Card</title>
<link href="https://fonts.googleapis.com/css2?family=Lato:wght@400;700&family=Montserrat:wght@400;500&display=swap" rel="stylesheet">
<style>
  :root {
    --backdrop: #2a2a2a;
    --card-light: #ffffff;
    --card-dark: #231f20;
    --ink: #1c1c1c;
    --ink-soft: #3a3a3a;
    --ink-reverse: #d9d9d9;
    --rule: #2b2b2b;
  }
  * { margin: 0; padding: 0; box-sizing: border-box; }
  html, body {
    width: 1200px; height: 866px; overflow: hidden;
    background: var(--backdrop);
  }
  .sheet {
    position: relative; width: 1200px; height: 866px;
    display: flex; flex-direction: column; align-items: center; justify-content: center;
    gap: 54px;
  }
  .card {
    position: relative; width: 660px; height: 377px;
    box-shadow: 0 10px 28px rgba(0,0,0,.45);
  }
  .card--front { background: var(--card-light); color: var(--ink); }
  .card--back { background: var(--card-dark); color: var(--ink-reverse); }

  .brand {
    position: absolute; display: flex; align-items: center; gap: 18px;
    font-family: "Montserrat", sans-serif; font-weight: 400;
  }
  .brand__square { border: 2px solid currentColor; flex: none; }
  .brand__name { display: flex; flex-direction: column; line-height: 1; }
  .brand__main { letter-spacing: .12em; }
  .brand__sub { letter-spacing: .5em; margin-top: 8px; }

  .card--front .brand { left: 270px; top: 92px; }
  .card--front .brand__square { width: 78px; height: 78px; }
  .card--front .brand__main { font-size: 27px; }
  .card--front .brand__sub { font-size: 11px; padding-left: 80px; }

  .card--back .brand {
    left: 0; right: 0; top: 78px; flex-direction: column; gap: 26px;
  }
  .card--back .brand__square { width: 112px; height: 112px; border-width: 2px; }
  .card--back .brand__name { align-items: center; }
  .card--back .brand__main { font-size: 30px; }
  .card--back .brand__sub { font-size: 12px; margin-top: 10px; }

  .person {
    position: absolute; left: 42px; top: 150px;
    font-family: "Lato", sans-serif;
  }
  .person__name { font-weight: 700; font-size: 19px; letter-spacing: .04em; }
  .person__role { font-size: 14px; color: var(--ink-soft); margin-top: 3px; }

  .divider {
    position: absolute; left: 262px; top: 170px; width: 300px; height: 1px;
    background: var(--rule);
  }

  .contacts {
    position: absolute; left: 42px; top: 210px; list-style: none;
    font-family: "Lato", sans-serif; font-size: 14.5px;
  }
  .contacts li { display: flex; align-items: center; gap: 8px; margin-bottom: 6px; }
  .contacts svg { width: 16px; height: 16px; flex: none; }

  .address {
    position: absolute; right: 74px; bottom: 52px; text-align: right;
    font-family: "Lato", sans-serif; font-size: 15px; line-height: 1.35;
  }
</style>
</head>
<body>
<main class="sheet">

  <section class="card card--front" aria-label="Business card front">
    <div class="brand">
      <span class="brand__square" aria-hidden="true"></span>
      <span class="brand__name">
        <span class="brand__main">BRIGHTNEST</span>
        <span class="brand__sub">DWELLING</span>
      </span>
    </div>

    <div class="person">
      <p class="person__name">MARCUS ELLERY</p>
      <p class="person__role">Managing Director</p>
    </div>

    <span class="divider" aria-hidden="true"></span>

    <ul class="contacts">
      <li>
        <svg viewBox="0 0 16 16" aria-hidden="true"><rect x=".75" y=".75" width="14.5" height="14.5" rx="2.5" fill="none" stroke="#1c1c1c" stroke-width="1.3"/><path d="M5 4.2l1.6-.4.9 2-1 .8a5.5 5.5 0 0 0 2.3 2.3l.8-1 2 .9-.4 1.6c-3.6.2-6.4-2.6-6.2-6.2z" fill="#1c1c1c"/></svg>
        044-987 654 321
      </li>
      <li>
        <svg viewBox="0 0 16 16" aria-hidden="true"><rect x=".75" y=".75" width="14.5" height="14.5" rx="2.5" fill="none" stroke="#1c1c1c" stroke-width="1.3"/><rect x="3.5" y="5" width="9" height="6.2" fill="#1c1c1c"/><path d="M3.5 5l4.5 3.5L12.5 5" fill="none" stroke="#fff" stroke-width=".9"/></svg>
        hello@brightnest.com
      </li>
      <li>
        <svg viewBox="0 0 16 16" aria-hidden="true"><rect x=".75" y=".75" width="14.5" height="14.5" rx="2.5" fill="none" stroke="#1c1c1c" stroke-width="1.3"/><circle cx="8" cy="8" r="4.3" fill="none" stroke="#1c1c1c" stroke-width="1"/><ellipse cx="8" cy="8" rx="1.8" ry="4.3" fill="none" stroke="#1c1c1c" stroke-width=".8"/><path d="M3.7 8h8.6" stroke="#1c1c1c" stroke-width=".8"/></svg>
        www.brightnestdwelling.com
      </li>
    </ul>

    <address class="address" style="font-style:normal">
      88, Harbour Row Lane<br>
      Eastvale, 30917
    </address>
  </section>

  <section class="card card--back" aria-label="Business card back">
    <div class="brand">
      <span class="brand__square" aria-hidden="true"></span>
      <span class="brand__name">
        <span class="brand__main">BRIGHTNEST</span>
        <span class="brand__sub">DWELLING</span>
      </span>
    </div>
  </section>

</main>
</body>
</html>
```